Business card design for Plumbing and Gas fitting company

We need a business card design for our plumbing and gas fitting company using the company logo and director details. Design should be modern and eye-catching however kept reasonably simple. This design should be targeted at commercial businesses/work so professionalism is key.

Target Market(s)

Commercial/business

Industry/Entity Type

Plumbing

Contact Information for Business Card

Warren Dohey
Director
027 581 9043
warren@vantorplumbingandgas.example
PO Box 7816
Palmerston North 4472

Font styles to use
Sans Serif

Requirements
Must have
• Logo
• Modern
• Kept simple
Nice to have
• Colour scheme based around logo

```html
<!DOCTYPE html>
<html lang="en">
<head>
<meta charset="utf-8">
<title>Vantor Plumbing &amp; Gas — Business Card</title>
<link rel="stylesheet" href="https://fonts.googleapis.com/css2?family=Exo+2:wght@400;600&family=Open+Sans:wght@400&display=swap">
<style>
  :root {
    --stage: #e4e5e7;
    --card-black: #111213;
    --card-white: #ffffff;
    --steel: #8a8b8c;
    --brand-blue: #1a75bc;
    --brand-orange: #ee7b30;
    --text-light: #e6e6e6;
  }
  * { box-sizing: border-box; margin: 0; padding: 0; }
  html, body { width: 1200px; height: 800px; overflow: hidden; }
  body {
    background: var(--stage);
    display: flex;
    align-items: center;
    justify-content: center;
    gap: 60px;
    font-family: "Open Sans", sans-serif;
  }
  .card {
    position: relative;
    width: 525px;
    height: 300px;
    overflow: hidden;
    box-shadow: 0 8px 24px rgba(0,0,0,0.18);
  }

  /* Back side */
  .card--back { background: var(--card-black); }
  .card--back .brand-name {
    position: absolute;
    top: 112px;
    left: 0; right: 0;
    text-align: center;
    font-family: "Exo 2", sans-serif;
    font-weight: 600;
    font-size: 34px;
    color: var(--brand-blue);
    letter-spacing: 0.5px;
  }
  .card--back .steel-band {
    position: absolute;
    left: 0; right: 0;
    background: var(--steel);
  }
  .card--back .steel-band--thin { bottom: 78px; height: 5px; }
  .card--back .steel-band--thick { bottom: 38px; height: 16px; }

  /* Front side */
  .card--front { background: var(--card-white); }
  .card--front .dark-panel { position: absolute; inset: 0; }
  .card--front .brand-name {
    position: absolute;
    top: 34px;
    right: 34px;
    font-family: "Exo 2", sans-serif;
    font-weight: 600;
    font-size: 27px;
    color: var(--brand-blue);
  }
  .contact {
    position: absolute;
    left: 30px;
    top: 118px;
    color: var(--text-light);
  }
  .contact__name {
    font-family: "Exo 2", sans-serif;
    font-weight: 400;
    font-size: 27px;
    color: var(--brand-blue);
    display: flex; align-items: center; gap: 8px;
    line-height: 1.1;
  }
  .contact__role {
    font-family: "Exo 2", sans-serif;
    font-size: 17px;
    color: var(--brand-orange);
    margin: 0 0 8px 26px;
  }
  .contact__row {
    display: flex;
    align-items: flex-start;
    gap: 8px;
    font-size: 13px;
    line-height: 1.45;
  }
  .contact__row svg { flex: none; margin-top: 3px; }
</style>
</head>
<body>

  <section class="card card--back" aria-label="Business card back">
    <p class="brand-name">Vantor Plumbing &amp; Gas</p>
    <div class="steel-band steel-band--thin"></div>
    <div class="steel-band steel-band--thick"></div>
  </section>

  <section class="card card--front" aria-label="Business card front">
    <svg class="dark-panel" viewBox="0 0 525 300" preserveAspectRatio="none" aria-hidden="true">
      <path d="M0 105 L470 105 C455 150 430 200 432 300 L0 300 Z" fill="var(--card-black)"/>
    </svg>
    <p class="brand-name">Vantor Plumbing &amp; Gas</p>

    <div class="contact">
      <p class="contact__name">
        <svg width="18" height="18" viewBox="0 0 18 18" aria-hidden="true">
          <circle cx="9" cy="5" r="4" fill="var(--brand-orange)"/>
          <path d="M1 18 C1 11 17 11 17 18 Z" fill="var(--brand-orange)"/>
        </svg>
        Warren Dohey
      </p>
      <p class="contact__role">Director</p>

      <div class="contact__row">
        <svg width="12" height="14" viewBox="0 0 12 14" aria-hidden="true">
          <path d="M6 0 A5 5 0 0 1 11 5 C11 9 6 14 6 14 C6 14 1 9 1 5 A5 5 0 0 1 6 0 Z" fill="var(--brand-orange)"/>
          <circle cx="6" cy="5" r="2" fill="var(--card-black)"/>
        </svg>
        <span>PO Box 7816<br>Palmerston North 4472</span>
      </div>
      <div class="contact__row">
        <svg width="12" height="12" viewBox="0 0 12 12" aria-hidden="true">
          <path d="M2 0 L4.5 0 L5.5 3 L4 4.5 C5 6.5 5.5 7 7.5 8 L9 6.5 L12 7.5 L12 10 C12 11 11 12 10 12 C4.5 12 0 7.5 0 2 C0 1 1 0 2 0 Z" fill="var(--brand-orange)"/>
        </svg>
        <span>027 581 9043</span>
      </div>
      <div class="contact__row">
        <svg width="13" height="10" viewBox="0 0 13 10" aria-hidden="true">
          <rect x="0.5" y="0.5" width="12" height="9" fill="none" stroke="var(--brand-orange)"/>
          <path d="M0.5 0.5 L6.5 5.5 L12.5 0.5" fill="none" stroke="var(--brand-orange)"/>
        </svg>
        <span>warren@vantorplumbingandgas.example</span>
      </div>
    </div>
  </section>

</body>
</html>
```